Create a cover for English Grammar Workbook

This book describes a system to learn English in a proper way - we call it The ''Keystone Arc'' Method.

It focuses on not only teaching grammar and its structures, but also giving students tips on how to use it and the best ways to remember what they learn.

The cover should have 3 realistic pillars (3D), with one closer to the front to show that this book is the 1st (front) Pillar.

The title is: "Speaking Clearly Every Day: *A Gentle Path toward Fluency"*

Author's name: Dorian Welch

```html
<!DOCTYPE html>
<html lang="en">
<head>
<meta charset="utf-8">
<title>Speaking Clearly Every Day — Cover</title>
<link rel="stylesheet" href="https://fonts.googleapis.com/css2?family=Montserrat:wght@600;700&family=Oswald:wght@500&display=swap">
<style>
  :root {
    --backdrop: #e9e9e9;
    --cover-dark: #393b41;
    --brand-red: #e0141b;
    --label-white: #f2f2f2;
    --label-ink: #2b2c30;
    --title-white: #f4f4f4;
    --author-grey: #e4e4e4;
    --column-light: #dedede;
    --column-shade: #a9abb0;
  }
  * { margin: 0; padding: 0; box-sizing: border-box; }
  html, body {
    width: 1200px;
    height: 2429px;
    overflow: hidden;
    background: var(--backdrop);
  }
  .canvas {
    position: relative;
    width: 1200px;
    height: 2429px;
    background: var(--backdrop);
  }
  .cover {
    position: absolute;
    left: 100px;
    top: 302px;
    width: 1000px;
    height: 1825px;
    background: var(--cover-dark);
    overflow: hidden;
  }
  .title-band {
    position: absolute;
    left: 0;
    top: 100px;
    width: 100%;
    height: 455px;
    background: var(--brand-red);
  }
  .mid-band {
    position: absolute;
    left: 0;
    top: 1044px;
    width: 100%;
    height: 162px;
    background: var(--brand-red);
  }
  .label {
    position: absolute;
    left: 50%;
    transform: translateX(-50%);
    background: var(--label-white);
    color: var(--label-ink);
    border: 5px solid #bdbdbd;
    border-radius: 14px;
    font-family: "Oswald", sans-serif;
    font-weight: 500;
    text-transform: uppercase;
    white-space: nowrap;
    line-height: 1;
  }
  .label--kicker {
    top: 60px;
    padding: 14px 34px;
    font-size: 62px;
  }
  .label--subtitle {
    top: 552px;
    padding: 14px 30px;
    font-size: 54px;
  }
  .main-title {
    position: absolute;
    left: 0;
    top: 178px;
    width: 100%;
    text-align: center;
    font-family: "Montserrat", sans-serif;
    font-weight: 600;
    color: var(--title-white);
    text-transform: uppercase;
    line-height: 1;
  }
  .main-title span { display: block; }
  .main-title .line-one { font-size: 176px; }
  .main-title .line-two { font-size: 176px; margin-top: 14px; }
  .columns-art {
    position: absolute;
    left: 145px;
    top: 660px;
    width: 710px;
    height: 940px;
    border-radius: 8px;
    background: linear-gradient(180deg, var(--column-light) 0%, var(--column-shade) 100%);
  }
  .author {
    position: absolute;
    left: 0;
    top: 1665px;
    width: 100%;
    text-align: center;
    font-family: "Montserrat", sans-serif;
    font-weight: 700;
    font-size: 88px;
    letter-spacing: 2px;
    color: var(--author-grey);
    text-transform: uppercase;
    line-height: 1;
  }
</style>
</head>
<body>
  <div class="canvas">
    <section class="cover">
      <div class="title-band"></div>
      <div class="mid-band"></div>
      <div class="label label--kicker">Speaking Clearly</div>
      <h1 class="main-title">
        <span class="line-one">Every</span>
        <span class="line-two">Day</span>
      </h1>
      <div class="label label--subtitle">A Gentle Path toward Fluency</div>
      <div class="columns-art" role="img" aria-label="Three white classical marble pillars on square bases, the middle one standing closer to the front"></div>
      <p class="author">Dorian Welch</p>
    </section>
  </div>
</body>
</html>
```